1 Page Website Design For Diabetic Discount RX Card

~~I NEED A WEBSITE LANDING PAGE DESIGNED~~:

TITLE: GET UP TO 75% Off ALL YOUR DIABETIC SUPPLIES GUARANTEED
SUBITITLE: Never Pay Full Price For Your Diabetic Supplies Again!

~~FORM~~:
Choose Your Current Brand Of Diabetic Supplies That You Currently Use To See If They Are Covered Under Our Free Diabetic RX Assistance Program:

~~DROP DOWN MENU~~
Acarbose Up To 75% Off!

Verimbra Dux Up To 75% Off!

Verimbra Dux Xr Up To 54% Off!

Pelvo Up To 75% Off!

Borquell Up To 75% Off!

Tumisko Up To 75% Off!

Quisden Up To 75% Off!

Welvoke Up To 75% Off!

Zorpelline Up To 54% Off!

Zorpequin Up To 54% Off!

Zorpeta Up To 54% Off!

Calmivest Up To 75% Off!

Calmora Up To 75% Off!

Chlorpropamide Up To 75% Off!

Colesevelam Up To 75% Off!

Merrowin Up To 54% Off!

Qnrk Up To 75% Off!

Desmopressin 52% Off

Hostivel 74% Off

Pruntalex Up To 54% Off!
Sorvilk Up To 75% Off!

Delumbo Up To 75% Off!

Nuskavir Up To 75% Off!

Glimepiride 66% Off

Glipizide Up To 75% Off!

Glipizide Er Up To 75% Off!

Tremvalux Up To 75% Off!

Tremvalux Xr Up To 75% Off!

Brenzofil Up To 75% Off!

Brenzofil Xl Up To 75% Off!

Yestramor Up To 75% Off!

Kipolvan Up To 75% Off!

Glyburide Up To 75% Off!

Glyburide Micronized Up To 75% Off!
Ostrivel Up To 75% Off!

Pardow Up To 75% Off!

Vuntorek Up To 75% Off!

Restivon 50 50 Up To 75% Off!

Restivon Up To 75% Off!

Kavostra N Up To 75% Off!

Kavostra R Up To 75% Off!

Insulin Detemir Up To 75% Off!

Insulin Glulisine Up To 75% Off!

Pelsquorin Up To 75% Off!

Pelsquora Up To 75% Off!

Roblinex Up To 75% Off!

Roblinex Xr Up To 75% Off!

Roblivo Up To 75% Off!

Mespolure Up To 75% Off!

Wovrastelo Up To 75% Off!

Tilbemo Up To 75% Off!

Frastovane Xr Up To 75% Off!

Ovrink Up To 75% Off!

Sauprex Up To 75% Off!

Drunvelo Up To 54% Off!

Metformin 73% Off

Pastoquil Up To 54% Off!

Miglitol Up To 75% Off!

Ferbalick Up To 33% Off!

Nateglinide Up To 75% Off!

Ulvoria Up To 75% Off!

Zestrapol Up To 75% Off!

Zestrabin N Up To 75% Off!

Zestrabin R Up To 75% Off!

Zestrakor Up To 75% Off!

Zestraplum Up To 33% Off!

Brumvexa Up To 75% Off!

Tescavil Up To 54% Off!

Krudal Up To 75% Off!

Pioglitazone Up To 75% Off!

Pramlintide Up To 75% Off!

Wolbanix Up To 54% Off!

Wolbary Up To 75% Off!

Humbrek 20% Off

Repaglinide Up To 75% Off!

Sadvex Up To 75% Off!

Rosiglitazone Up To 75% Off!

Sitagliptin Up To 75% Off!

Plumvoy Up To 75% Off!

Garvostek Up To 75% Off!

Treskuvo Up To 75% Off!

Obrilcha Up To 75% Off!

Tolazamide Up To 75% Off!

Tolbutamide Up To 75% Off!

Vempruka Up To 54% Off!

Faskid Up To 75% Off!

Lurmobixa Up To 75% Off!

Qualmedo Up To 75% Off!

Sombrewick Up To 15% Off!

Vantoberry Up To 75% Off!

Dombrisel Up To 33% Off!

Harnupex Up To 75% Off!

Pidsarn Up To 75% Off!

Brafmel Xr Up To 75% Off!

~~~~After they choose one I want this message to pop up~~~~:

YES! ~~NAME OF DRUG~~ IS COVERED UNDER OUR FREE DIABETIC RX PROGRAM!
3 EASY WAYS TO RECEIVE YOUR FREE DIABETIC RX ASSISTANCE VOUCHER:

1. Simply Click Below To Download Your Voucher Right Now!

~~DOWNLOAD VOUCHER NOW~~
2. Enter Your Cell Phone Number And We Will Send The Voucher To You By Text Message Instantly:

3. Enter Your Email And We Will Send The Voucher To Your Email Instantly:

Target Market(s)

People with Diabetes

Number of Pages Required

1 page

Colors

Designer to choose colors to be used in the design.

Requirements
Must have
• must be professional looking and build trust and credibility
Nice to have
• Photos of diabetics...real people
Should not have
• red

```html
<!DOCTYPE html>
<html lang="en">
<head>
<meta charset="utf-8">
<title>Diabetic RX Assistance Program</title>
<link href="https://fonts.googleapis.com/css2?family=Lato:wght@400;700;900&family=Open+Sans:wght@400;600;700;800&display=swap" rel="stylesheet">
<style>
:root{
  --blue:#0f6fbd;
  --blue-light:#5d9fd3;
  --hero-a:#7fbde2;
  --hero-b:#4f97c8;
  --cta-a:#1b5573;
  --cta-b:#2b7391;
  --ink:#222b33;
  --muted:#7a7a7a;
  --field:#ececec;
  --band:#f3f6f9;
  --footer:#f1f5f8;
  --social:#9a9a9a;
  --white:#ffffff;
}
*{margin:0;padding:0;box-sizing:border-box}
html,body{width:1200px;height:2517px;overflow:hidden;background:var(--white)}
body{position:relative;font-family:"Open Sans",sans-serif;color:var(--ink)}
.abs{position:absolute}
.hero{left:0;top:0;width:1200px;height:574px;background:linear-gradient(120deg,var(--hero-a),var(--hero-b) 60%,#8cc3e3)}
.hero-photo{position:absolute;inset:0;background:radial-gradient(ellipse at 35% 30%,rgba(255,255,255,.18),transparent 55%),radial-gradient(ellipse at 80% 45%,rgba(255,255,255,.22),transparent 50%)}
.brand{font-family:"Lato",sans-serif;font-weight:900;font-size:34px;color:var(--white);left:104px;top:20px}
.nav a{position:absolute;top:30px;font-family:"Lato",sans-serif;font-weight:700;font-size:13px;color:var(--white);text-decoration:none}
.hero-title{left:0;width:1200px;top:236px;text-align:center;color:var(--white);font-weight:800;font-size:29px;letter-spacing:.3px}
.hero-sub{left:0;width:1200px;top:273px;text-align:center;color:var(--white);font-size:23px}
.pill{display:flex;align-items:center;justify-content:center;border-radius:30px;font-family:"Lato",sans-serif;font-size:15px}
.btn-start{left:433px;top:340px;width:163px;height:43px;background:var(--blue);color:var(--white)}
.btn-learn{left:604px;top:340px;width:163px;height:43px;background:var(--white);color:var(--blue)}
.intro{left:0;width:1200px;top:646px;text-align:center;font-size:21px;line-height:27px;color:var(--muted)}
.intro em{font-style:normal;color:var(--blue-light)}
.brand-list{left:107px;top:806px;list-style:none}
.brand-list li{height:53.7px;font-size:15.5px;color:var(--muted)}
.brand-list li.active{color:var(--blue)}
.more{left:107px;top:1665px;font-size:14px;color:var(--ink);text-decoration:underline}
.divider{left:426px;top:810px;width:1px;height:887px;background:#e2e2e2}
.band{left:426px;top:1069px;width:774px;height:203px;background:var(--band)}
.result-head{left:426px;width:748px;top:834px;text-align:center;font-weight:600;font-size:16.5px;line-height:27px;text-transform:uppercase}
.result-head b{color:#1e5f8a;font-weight:800}
.step{left:426px;width:710px;text-align:center;font-size:11px;color:var(--muted);font-weight:600}
.btn-download{left:700px;top:993px;width:162px;height:44px;background:var(--blue);color:var(--white)}
.field{left:612px;width:366px;height:42px;border-radius:22px;background:var(--field)}
.field span{position:absolute;left:38px;top:12px;font-size:11.5px;color:#8a8a8a}
.field .send{position:absolute;right:0;top:0;width:111px;height:42px;background:var(--blue);color:var(--white);font-size:15px}
.cta{left:0;top:1797px;width:1200px;height:364px;background:linear-gradient(100deg,var(--cta-a),var(--cta-b) 55%,var(--cta-a))}
.cta-title{left:0;width:1200px;top:1900px;text-align:center;font-family:"Lato",sans-serif;font-weight:900;font-size:37px;color:var(--white)}
.btn-voucher{left:391px;top:1982px;width:418px;height:62px;background:var(--white);color:var(--blue);font-weight:900;font-size:18px;letter-spacing:.5px}
.footer{left:0;top:2161px;width:1200px;height:356px;background:var(--footer)}
.foot-brand{left:138px;top:2213px;font-family:"Lato",sans-serif;font-weight:900;font-size:34px;color:var(--ink)}
.social{top:2274px;width:53px;height:53px;background:var(--social)}
.copy{left:138px;top:2436px;font-family:"Lato",sans-serif;font-size:13px;line-height:25px;color:var(--ink)}
.copy u{text-decoration:underline}
.foot-col{font-family:"Lato",sans-serif;top:2216px}
.foot-col h4{font-size:20px;font-weight:700;margin-bottom:22px}
.foot-col a{display:block;font-size:13px;color:var(--ink);text-decoration:none;height:48.5px}
</style>
</head>
<body>
<header class="abs hero">
  <div class="hero-photo" role="img" aria-label="Photo of a smiling older patient shaking hands with a nurse, tinted blue"></div>
</header>
<div class="abs brand">LOGO</div>
<nav class="nav">
  <a style="left:780px">Home</a>
  <a style="left:846px">Menu</a>
  <a style="left:910px">Page</a>
  <a style="left:968px">About</a>
  <a style="left:1035px">Contact</a>
</nav>
<h1 class="abs hero-title">GET UP TO 75% Off ALL YOUR DIABETIC SUPPLIES GUARANTEED</h1>
<p class="abs hero-sub">Never Pay Full Price For Your Diabetic Supplies Again!</p>
<a class="abs pill btn-start">START NOW</a>
<a class="abs pill btn-learn">LEARN MORE</a>

<p class="abs intro">Choose your current brand of <em>Diabetic Supplies</em> that you currently use<br>to see if they are covered under our free <em>Diabetic RX Assistance Program</em>:</p>

<ul class="abs brand-list">
  <li class="active">Acarbose Up To 75% Off!</li>
  <li>Verimbra Dux Up To 75% Off!</li>
  <li>Verimbra Dux Xr Up To 54% Off!</li>
  <li>Pelvo Up To 75% Off!</li>
  <li>Borquell Up To 75% Off!</li>
  <li>Tumisko Up To 75% Off!</li>
  <li>Quisden Up To 75% Off!</li>
  <li>Welvoke Up To 75% Off!</li>
  <li>Zorpelline Up To 54% Off!</li>
  <li>Zorpequin Up To 54% Off!</li>
  <li>Zorpeta Up To 54% Off!</li>
  <li>Calmivest Up To 75% Off!</li>
  <li>Calmora Up To 75% Off!</li>
  <li>Chlorpropamide Up To 75% Off!</li>
  <li>Colesevelam Up To 75% Off!</li>
  <li>Merrowin Up To 54% Off!</li>
</ul>
<a class="abs more">see 27+ more &gt;&gt;</a>
<div class="abs divider"></div>

<div class="abs band"></div>
<h2 class="abs result-head">Yes! <b>Acarbose</b> is covered under our free diabetic RX program!<br>3 easy ways to receive your free diabetic RX assistance voucher:</h2>

<p class="abs step" style="top:958px">1. Simply Click Below To Download Your Voucher Right Now!</p>
<a class="abs pill btn-download">DOWNLOAD</a>

<p class="abs step" style="top:1133px">2. Enter Your Cell Phone Number And We Will Send The Voucher To You By Text Message Instantly:</p>
<div class="abs field" style="top:1169px"><span>Enter phone here</span><a class="pill send">SEND</a></div>

<p class="abs step" style="top:1309px">3. Enter Your Email And We Will Send The Voucher To Your Email Instantly:</p>
<div class="abs field" style="top:1343px"><span>Enter e-mail address here</span><a class="pill send">SEND</a></div>

<section class="abs cta" role="img" aria-label="Photo of a patient checking blood sugar with a meter, tinted dark teal"></section>
<h2 class="abs cta-title">Never Pay Full Price For Your Diabetic Supplies Again!</h2>
<a class="abs pill btn-voucher">GET YOUR VOUCHER TODAY!</a>

<footer class="abs footer"></footer>
<div class="abs foot-brand">LOGO</div>
<div class="abs social" style="left:138px" role="img" aria-label="Social network link"></div>
<div class="abs social" style="left:196px" role="img" aria-label="Social network link"></div>
<div class="abs social" style="left:255px" role="img" aria-label="Social network link"></div>
<p class="abs copy">Copyright © 2008 - 2017 Company Name, LLC.<br>All rights reserved. <u>See additional information.</u></p>

<div class="abs foot-col" style="left:569px">
  <h4>Policy</h4>
  <a>Privacy Policy</a><a>Terms of Use</a><a>Contact Us</a><a>About us</a><a>Vouchers</a>
</div>
<div class="abs foot-col" style="left:740px">
  <h4>About</h4>
  <a>About</a><a>Careers</a><a>Newsletter</a><a>Health Services</a><a>Accessibility</a>
</div>
<div class="abs foot-col" style="left:925px">
  <h4>Vouchers</h4>
  <a>All Vouchers</a><a>Sales</a><a>New page</a><a>Health page</a><a>Accessibility</a>
</div>
</body>
</html>
```